Updated business card

I would like to change the picture on the existing design. Please use the attached photo. Remove my last name from the logo and have that appear (just my first name with the lock symbol [trademarked]) appear horizontally or vertically? on the front of the card. My company information has changed on the back of the card. It should be "Brindle" instead of "Orbit 58 Fernhollow Realty", 4275 Pellham Blvd. Arlington, VA 22209 is the new address. The Orbit 58 Fernhollow logo should be replaced with the Brindle logo which is attached as well. I am using Zib cards with the rounded edges for printing so the size is larger than the typically business card. The colors should remain consistent with what I have but can be used differently.

```html
<!DOCTYPE html>
<html lang="en">
<head>
<meta charset="utf-8">
<title>Delphine Marlowe – Business Card</title>
<link rel="stylesheet" href="https://fonts.googleapis.com/css2?family=Montserrat:wght@400;500;700&family=Yellowtail&display=swap">
<style>
  :root {
    --stage: #1e1e1e;
    --magenta: #d4118b;
    --ink: #0a0a0a;
    --white: #ffffff;
    --photo-top: #d9d4d2;
    --photo-mid: #a85a33;
    --photo-low: #5a3a2a;
  }
  * { margin: 0; padding: 0; box-sizing: border-box; }
  html, body { width: 1200px; height: 1000px; overflow: hidden; }
  body {
    background: var(--stage);
    font-family: "Montserrat", Arial, sans-serif;
    position: relative;
  }
  .card {
    position: absolute;
    top: 153px;
    width: 463px;
    height: 692px;
    background: var(--ink);
    overflow: hidden;
  }
  .card--front { left: 111px; }
  .card--back { left: 611px; width: 465px; }

  .line {
    position: absolute;
    left: 0; right: 0;
    text-align: center;
    transform: translateY(-50%);
    white-space: nowrap;
  }

  /* Front */
  .portrait {
    height: 506px;
    background: linear-gradient(170deg, var(--photo-top) 0%, #c9a592 35%, var(--photo-mid) 65%, var(--photo-low) 100%);
  }
  .brand-name {
    top: 574px;
    color: var(--white);
    font-weight: 400;
    font-size: 48px;
    letter-spacing: 2px;
  }
  .tagline {
    top: 634px;
    color: var(--white);
    font-family: "Yellowtail", cursive;
    font-size: 34px;
  }

  /* Back */
  .contact-panel {
    position: absolute;
    left: 0; top: 0; right: 0;
    height: 504px;
    background: var(--magenta);
    color: var(--ink);
  }
  .agent-name { top: 77px; font-weight: 700; font-size: 20px; letter-spacing: 0.8px; }
  .agent-role { top: 109px; font-family: "Yellowtail", cursive; font-size: 26px; }
  .agent-credential { top: 136px; font-size: 16px; letter-spacing: 0.5px; }
  .contact-icon { position: absolute; left: 50%; margin-left: -21px; }
  .contact-icon--mail { top: 179px; }
  .contact-icon--phone { top: 278px; }
  .contact-icon--web { top: 382px; }
  .contact-text { font-size: 21px; letter-spacing: 0.3px; }
  .contact-text--mail { top: 243px; }
  .contact-text--phone { top: 345px; }
  .contact-text--web { top: 447px; }

  .office {
    font-style: normal;
    color: var(--white);
    font-weight: 500;
    font-size: 20px;
    line-height: 27px;
    top: 547px;
  }
  .office-brands {
    position: absolute;
    left: 0; right: 0; top: 601px;
    display: flex; justify-content: center; align-items: center; gap: 46px;
    height: 52px;
  }
  .brokerage {
    color: var(--white);
    font-size: 21px;
    font-weight: 500;
    letter-spacing: 3px;
  }
  .housing-badge {
    width: 50px; height: 50px;
    background: var(--white);
  }
</style>
</head>
<body>
  <section class="card card--front">
    <div class="portrait" role="img" aria-label="Portrait photo of the realtor"></div>
    <div class="line brand-name">DELPHINE</div>
    <div class="line tagline">Homes, Thoughtfully Found.</div>
  </section>

  <section class="card card--back">
    <div class="contact-panel">
      <div class="line agent-name">DELPHINE MARLOWE, J.D., LL.M.</div>
      <div class="line agent-role">Realtor</div>
      <div class="line agent-credential">Accredited Staging Professional</div>

      <svg class="contact-icon contact-icon--mail" width="42" height="42" viewBox="0 0 42 42" aria-hidden="true">
        <circle cx="21" cy="21" r="19" fill="none" stroke="#fff" stroke-width="2.5"/>
        <rect x="11" y="14" width="20" height="14" fill="#fff"/>
        <path d="M11 14 L21 22 L31 14" fill="none" stroke="#d4118b" stroke-width="1.6"/>
      </svg>
      <div class="line contact-text contact-text--mail">Delphine@DelphineMarlowe.com</div>

      <svg class="contact-icon contact-icon--phone" width="42" height="42" viewBox="0 0 42 42" aria-hidden="true">
        <circle cx="21" cy="21" r="19" fill="none" stroke="#fff" stroke-width="2.5"/>
        <path d="M14 11 L18 11 L20 16 L17.5 18 C19 21.5 20.5 23 24 24.5 L26 22 L31 24 L31 28 C31 29.5 29.5 31 28 31 C19 30 12 23 11 14 C11 12.5 12.5 11 14 11 Z" fill="#fff"/>
      </svg>
      <div class="line contact-text contact-text--phone">202.555.0147</div>

      <svg class="contact-icon contact-icon--web" width="42" height="42" viewBox="0 0 42 42" aria-hidden="true">
        <circle cx="21" cy="21" r="19" fill="none" stroke="#fff" stroke-width="2.5"/>
        <circle cx="15" cy="27" r="2.6" fill="#fff"/>
        <path d="M13 19 A10 10 0 0 1 23 29" fill="none" stroke="#fff" stroke-width="3"/>
        <path d="M13 13 A16 16 0 0 1 29 29" fill="none" stroke="#fff" stroke-width="3"/>
      </svg>
      <div class="line contact-text contact-text--web">DelphineMarlowe.com</div>
    </div>

    <address class="line office">4275 Pellham Blvd.<br>Arlington, VA 22209</address>
    <div class="office-brands">
      <span class="brokerage">BRINDLE</span>
      <span class="housing-badge" role="img" aria-label="Equal housing badge"></span>
    </div>
  </section>
</body>
</html>
```